Cybersecurity company is looking for business card.

I need a business card design for our company, we are a cybersecurity company providing advance technology to protect agains any kind of malware. We need a fresh modern design it should communicate modern, technology and growth.

Target Market(s)

Business to business

Industry/Entity Type

Business

Contact Information for Business Card

Should have location, address, fax, mobile, phone, email and website.

Requirements
Must have
• Must follow company's logo color and style. Must have the company's log on its.

```html
<!DOCTYPE html>
<html lang="en">
<head>
<meta charset="utf-8">
<title>Velnara Business Card</title>
<link rel="stylesheet" href="https://fonts.googleapis.com/css2?family=Tinos:wght@400;700&display=swap">
<style>
  :root {
    --brand-red: #a3202a;
    --card-white: #f4f4f2;
    --ink: #141414;
    --muted: #5a5a5a;
    --backdrop: #e6e3de;
  }
  * { margin: 0; padding: 0; box-sizing: border-box; }
  html, body { width: 1200px; height: 892px; overflow: hidden; }
  body {
    background: var(--backdrop);
    font-family: "Tinos", "Times New Roman", serif;
    color: var(--ink);
    display: flex;
    align-items: center;
    justify-content: center;
    gap: 40px;
  }
  .card {
    position: relative;
    width: 540px;
    height: 309px;
    background: var(--card-white);
    overflow: hidden;
    box-shadow: 0 6px 18px rgba(0,0,0,0.18);
  }
  .card-shapes { position: absolute; inset: 0; width: 100%; height: 100%; }
  .card-shapes polygon { fill: var(--brand-red); }

  /* Back */
  .card-back .wordmark {
    position: absolute;
    left: 100px;
    top: 112px;
    font-size: 74px;
    font-weight: 700;
    color: var(--ink);
    letter-spacing: 1px;
    line-height: 1;
  }

  /* Front */
  .card-front .wordmark {
    position: absolute;
    right: 40px;
    top: 26px;
    font-size: 62px;
    font-weight: 700;
    color: var(--ink);
    letter-spacing: 1px;
    line-height: 1;
  }
  .person {
    position: absolute;
    left: 118px;
    top: 152px;
    white-space: nowrap;
  }
  .person-name { font-size: 23px; font-weight: 700; color: #2a2a2a; line-height: 1.1; }
  .person-role { font-size: 11px; color: var(--muted); margin-top: 3px; }
  .divider {
    position: absolute;
    left: 300px;
    top: 146px;
    width: 1px;
    height: 124px;
    background: var(--ink);
  }
  .contact-list {
    position: absolute;
    left: 313px;
    top: 144px;
    list-style: none;
    font-size: 12px;
    line-height: 1.4;
    white-space: nowrap;
  }
  .contact-list li { display: flex; align-items: flex-start; gap: 7px; }
  .contact-list svg { width: 10px; height: 10px; margin-top: 3px; flex: none; }
  .contact-list svg * { fill: none; stroke: var(--ink); stroke-width: 1.4; }
  .contact-list svg .solid { fill: var(--ink); stroke: none; }
</style>
</head>
<body>

  <section class="card card-back" aria-label="Business card back">
    <svg class="card-shapes" viewBox="0 0 540 309" preserveAspectRatio="none" aria-hidden="true">
      <polygon points="150,0 540,0 540,150 330,309 0,309 0,120"/>
    </svg>
    <div class="wordmark">Velnara</div>
  </section>

  <section class="card card-front" aria-label="Business card front">
    <svg class="card-shapes" viewBox="0 0 540 309" preserveAspectRatio="none" aria-hidden="true">
      <polygon points="0,0 120,0 45,309 0,309"/>
      <polygon points="540,120 540,309 497,309"/>
    </svg>
    <div class="wordmark">Velnara</div>

    <div class="person">
      <div class="person-name">Employee name</div>
      <div class="person-role">Managing Director</div>
    </div>
    <div class="divider"></div>

    <ul class="contact-list">
      <li><svg viewBox="0 0 10 10"><path d="M5 9.5 C2 6 2 4.5 2 3.8 A3 3 0 0 1 8 3.8 C8 4.5 8 6 5 9.5Z"/></svg>Coral Bay - UAE</li>
      <li><svg viewBox="0 0 10 10"><rect x="2.5" y="0.8" width="5" height="8.4" rx="0.8"/></svg>+971 52 123 XXXX</li>
      <li><svg viewBox="0 0 10 10"><path class="solid" d="M2 1 L4 1 L4.6 3 L3.4 4 C4 5.5 4.6 6.1 6 6.6 L7 5.4 L9 6 L9 8 C5 8.5 1.5 5 2 1Z"/></svg>04 123 XXXX</li>
      <li><svg viewBox="0 0 10 10"><rect x="1" y="4" width="8" height="4.5"/><rect x="2.8" y="1" width="4.4" height="3"/></svg>04 123 XXXX</li>
      <li><svg viewBox="0 0 10 10"><circle cx="5" cy="5" r="4"/><path d="M1 5 H9 M5 1 C3 3.5 3 6.5 5 9 M5 1 C7 3.5 7 6.5 5 9"/></svg>www.velnara.com</li>
      <li><svg viewBox="0 0 10 10"><rect x="1" y="2" width="8" height="6"/><path d="M1 2 L5 5.5 L9 2"/></svg>name.surname@velnara.com</li>
      <li><svg viewBox="0 0 10 10"><path class="solid" d="M5 1 L9.5 5 L8 5 L8 9 L6 9 L6 6.5 L4 6.5 L4 9 L2 9 L2 5 L0.5 5Z"/></svg><span>Harbor Tech Park<br>(HTP) -Coral Bay Road.</span></li>
    </ul>
  </section>

</body>
</html>
```